Hollowmere Yuletide Firs needs words putting into pictures!

Hollowmere Yuletide Firs sells real Christmas Trees directly to consumers and retailers. A "growing" part of our business is fulfilling online orders e.g. a garden centre sells a tree online, and we do everything else from selecting the tree to delivery. We are now looking to market this service as best in class due to the selection process we have, and a link up we have made with a courier company.

We want to summarise the process into a simple one page graphic that illustrates the process from start to finish in simple language, short sentences, with images and pictures.

Given how difficult it is to get good images of Christmas trees, we thought simple outline pictures could work - almost like sketches. We are open to all ideas.

We can provide any of the images in the attached brochure, and many more depending what you may require.

We like clean cut, simple designs that are clear and innovative.

Contact Information for Business Card

Simon Carver, Director, Hollowmere Yuletide Firs, simon@hollowmereyuletidefirs.example, Brackwell Croft Farm, Brackwell Croft Lane, Thistleby Moor, QX4 8TD

Font styles to use
Sans Serif

Colors
00a990

Requirements
Must have
• Condense the info down into a manageable graphic that shows our customers clearly what service we are able to provide
Nice to have
• Simple, elegant design to compliment brand feel
Should not have
• Not be too complicated

```html
<!DOCTYPE html>
<html lang="en">
<head>
<meta charset="utf-8">
<title>Hollowmere Yuletide Firs – Online Delivery Service</title>
<link href="https://fonts.googleapis.com/css2?family=Lato:wght@400;700&display=swap" rel="stylesheet">
<style>
  :root{
    --green:#2f8a3c;
    --green-dark:#1d6b30;
    --green-light:#8cc63f;
    --green-pale:#d7ead0;
    --navy:#2e2b6b;
    --ink:#1e1e1e;
    --rule:#3a3a3a;
    --paper:#ffffff;
  }
  *{box-sizing:border-box;margin:0;padding:0}
  html,body{width:1200px;height:900px;overflow:hidden;background:var(--paper)}
  body{position:relative;font-family:"Lato",sans-serif;color:var(--ink)}
  .page{position:absolute;top:94px;height:705px;border:1px solid var(--rule);background:var(--paper)}
  .page--process{left:40px;width:545px}
  .page--story{left:615px;width:547px}

  .brand{position:absolute;text-align:center;color:var(--navy);font-weight:700;line-height:1.15;letter-spacing:.04em}
  .brand__mark{display:block;width:14px;height:14px;border-radius:50%;background:var(--green);margin:0 auto 8px}
  .page--process .brand{left:60px;top:105px;width:150px;font-size:18px}
  .page--story .brand{left:70px;top:100px;width:140px;font-size:18px}

  .service-title{position:absolute;left:30px;top:168px;width:210px;text-align:center;font-size:14px;font-weight:400}
  .divider{position:absolute;left:271px;top:76px;width:1px;height:540px;background:var(--rule)}

  .step{position:absolute;width:232px;font-size:10px;line-height:13.5px}
  .step p+p{margin-top:13px}
  .step__num{color:var(--green);font-weight:700;font-size:11px}
  .step__icon{float:left;margin:2px 12px 4px 0;background:linear-gradient(135deg,var(--green-pale),#b7d9a8);border-radius:3px}
  .step--1{left:24px;top:200px}
  .step--2{left:24px;top:290px}
  .step--3{left:24px;top:388px}
  .step--4{left:24px;top:508px}
  .step--5{left:290px;top:74px}
  .step--6{left:290px;top:230px}
  .step--7{left:290px;top:375px}
  .step--8{left:290px;top:525px}

  .footer{position:absolute;left:0;right:0;top:646px;text-align:center;color:var(--green);font-size:10px;line-height:13px}

  .why{position:absolute;left:214px;top:90px;font-size:10px;line-height:14px}
  .why h2{font-size:15px;font-weight:400;margin-bottom:4px}
  .why ul{list-style:none}
  .why li::before{content:"• "}
  .why em{font-style:italic}
  .why .indent{padding-left:7px}

  .banner{position:absolute;left:30px;top:226px;width:490px;height:98px;border-radius:40px 0 0 0;
    background:linear-gradient(180deg,#cfe6b8 0%,#8cc63f 45%,#2f8a3c 100%)}

  .story{position:absolute;left:30px;top:342px;width:492px;font-size:10px;line-height:13.5px;text-align:justify}
  .story p+p{margin-top:13px}
</style>
</head>
<body>

<section class="page page--process">
  <div class="brand"><span class="brand__mark"></span>Hollowmere Yuletide Firs</div>
  <h1 class="service-title">Online Delivery Service</h1>
  <div class="divider"></div>

  <div class="step step--1">
    <div class="step__icon" role="img" aria-label="Outline sketch of hills with small fir trees and a flag" style="width:90px;height:40px"></div>
    <p><span class="step__num">1.</span> We view the trees several times per year in Scotland, and choose which fields and plantations our trees will be cut from.</p>
  </div>

  <div class="step step--2">
    <div class="step__icon" role="img" aria-label="Outline sketch of three fir trees with a tick beneath" style="width:70px;height:48px"></div>
    <p><span class="step__num">2.</span> We choose specific premium quality trees and label them in the field in September time to ensure our customers receive only the very best trees.</p>
  </div>

  <div class="step step--3">
    <div class="step__icon" role="img" aria-label="Outline sketch of a truck carrying a Christmas tree" style="width:80px;height:40px"></div>
    <p><span class="step__num">3.</span> The trees are cut between the end of November and mid December, depending upon the proposed delivery date. They are transported to a farm where they are measured and graded for a second time. the trunk is cut and placed in water so that the tree can begin drinking again.</p>
  </div>

  <div class="step step--4">
    <div class="step__icon" role="img" aria-label="Fir tree with measuring arrows and a tick" style="width:78px;height:58px"></div>
    <p><span class="step__num">4.</span> Every tree is hand picked for each customer. Two days before the delivery date, the tree is selected and checked for a third time to make sure that it meets the size and quality specifications, and any special requests which have been made.</p>
  </div>

  <div class="step step--5">
    <div class="step__icon" role="img" aria-label="Outline sketch of a netted tree with a label tag" style="width:58px;height:78px"></div>
    <p><span class="step__num">5.</span> The tree is then labelled for the customer and netted through a Christmas tree netting funnel to make it easier to handle and transport. Packaged in a special tree transport bag, full protection for the tree is provided.</p>
  </div>

  <div class="step step--6">
    <div class="step__icon" role="img" aria-label="Outline sketch of a cut tree trunk end" style="width:68px;height:50px"></div>
    <p><span class="step__num">6.</span> As close as possible to dispatch 2cm is chopped off the bottom of the tree - this opens the tree up and means it is more likely to drink water when in a water holding stand.</p>
    <p>The tree is dispatched the working day before it is due for delivery to keep the time spent in transit to a minimum and maximise freshness.</p>
  </div>

  <div class="step step--7">
    <div class="step__icon" role="img" aria-label="Monitor, phone and clock icons" style="width:78px;height:66px"></div>
    <p><span class="step__num">7.</span> The customer receives texts/emails throughout the day of their delivery to update on the progress of the driver. If possible, the driver will call 30 mins before delivery</p>
  </div>

  <div class="step step--8">
    <div class="step__icon" role="img" aria-label="Fir tree beside a calendar" style="width:78px;height:46px"></div>
    <p><span class="step__num">8.</span> Trees are cut at regular intervals throughout December to ensure that we constantly have a fresh supply of Christmas trees, and to reduce the time between the tree being cut, and it being delivered to the customer.</p>
  </div>

  <div class="footer">sales@hollowmereyuletidefirs.example<br>www.hollowmereyuletidefirs.example</div>
</section>

<section class="page page--story">
  <div class="brand"><span class="brand__mark"></span>Hollowmere Yuletide Firs</div>

  <div class="why">
    <h2>Why Choose Us?</h2>
    <ul>
      <li>Full customer service support</li>
      <li>Efficient transport - <em>Monday to Sunday Delivery</em></li>
      <li>Damage prevention - <em>Bespoke tree transport bag (branded)</em></li>
      <li>Careful selection with multiple stages of quality control<br><span class="indent">where the Trees are Grown</span></li>
    </ul>
  </div>

  <div class="banner" role="img" aria-label="Landscape of rolling green fields with rows of fir trees"></div>

  <div class="story">
    <p>Every tree has a story. Each plantation and field we harvest trees from has specific characteristics that display in the trees. A number of factors affect this – the location of the forest and local weather conditions, the type and composition of the soil, the type and provenance of seedlings used and the specialist skills of each grower.</p>
    <p>Each type of tree requires very careful management and growing premium quality Christmas trees is a skilled and rare profession.</p>
    <p>Our Nordmann fir trees (up to 8 feet) are grown on the edge of a small village hidden deep in the Scottish borders on a farm that has produced some of the best trees available each and every year. A dedicated team has perfected the art of nurturing the trees in their early years, before using a specialist hand pruning method to shape them into perfect specimens.</p>
    <p>Our Fraser Fir trees are grown on a rather inaccessible piece of land called Dyke Foot in the heart of Scotland. Dyke Foot is an area at the top of a hill with fantastic views and is only accessible on foot or by tractor – it is not a place you can stumble upon. This land has a rather unique composition, which makes inhospitable for most plant life, but ideal for Fraser Fir. Our larger trees are grown on two farms deep in the hills beyond Loch Lomond, and near the coast north of Fife. They are carefully tended to for over ten years using a range of special equipment to give a lovely shape. By using a combination of locations for our trees, we can rely on the specialisms of each grower, and provide a resilient and consistent supply. We can also be flexible with the harvest of the tree and adapt to the local weather conditions to make sure that the trees have had sufficient frost before being cut.</p>
  </div>

  <div class="footer">sales@hollowmereyuletidefirs.example<br>www.hollowmereyuletidefirs.example</div>
</section>

</body>
</html>
```